Simple+Professional tech feel + warm and friendly box design for pet test kit

Project Name: 10-Minute Canine & Feline Rapid Test Kit Packaging Design
Target Brand Reference: VETRALUX (South Korea) styles
Design Style Direction: Professional tech feel + warm and friendly
Professionalism (Professional): Clear typography and distinct information hierarchy to reflect the product’s scientific rigor and accuracy.
Technological: Reflected through clean graphics and a minimalist layout.
Friendly: Utilise soft, warm colour combinations to convey care for pets and well-wishes for their health.
International: The design should align with mainstream aesthetics and avoid cultural ambiguities.

Target Market(s)
European Union and the United States
Industry/Entity Type
Veterinary Medical
Look and feel
Each slider illustrates characteristics of the customer's brand and the style your logo design should communicate.

```html
<!DOCTYPE html>
<html lang="en">
<head>
<meta charset="utf-8">
<title>Lumora 10-Minute Canine &amp; Feline Rapid Test Kit – Packaging</title>
<link rel="stylesheet" href="https://fonts.googleapis.com/css2?family=Varela+Round&family=Fira+Sans:ital,wght@0,500;0,700;1,500&display=swap">
<style>
  :root {
    --green: #62a945;
    --green-light: #7cc556;
    --green-line: #6dba4c;
    --orange: #f05a28;
    --orange-light: #f7793d;
    --white: #ffffff;
    --stage: #eeeff1;
    --ink-soft: #e9f4e2;
  }
  * { box-sizing: border-box; margin: 0; padding: 0; }
  html, body { width: 718px; height: 1200px; overflow: hidden; }
  body {
    background: var(--stage);
    font-family: "Varela Round", "Fira Sans", sans-serif;
    position: relative;
  }

  /* Top lid */
  .panel-top {
    position: absolute; left: 29px; top: 110px; width: 660px; height: 200px;
    background: linear-gradient(90deg, var(--green) 0%, #6aae48 60%, var(--green) 100%);
    display: flex; flex-direction: column; align-items: center; justify-content: center;
  }
  .lid-brand {
    font-family: "Varela Round", sans-serif;
    color: var(--ink-soft);
    font-size: 44px; letter-spacing: 1px; line-height: 1;
  }
  .lid-rule { width: 200px; height: 1px; background: var(--ink-soft); margin: 8px 0 6px; }
  .lid-tagline { color: var(--ink-soft); font-size: 8px; letter-spacing: .5px; }

  /* Front panel */
  .panel-front {
    position: absolute; left: 29px; top: 310px; width: 660px; height: 250px;
    background: var(--white);
  }
  .front-brand {
    position: absolute; left: 40px; top: 42px;
    font-family: "Varela Round", sans-serif;
    color: var(--green); font-size: 46px; line-height: 1;
  }
  .front-brand sup { font-size: 13px; vertical-align: top; margin-left: 3px; }
  .badge-tests {
    position: absolute; right: 18px; top: 95px; height: 22px; padding: 0 10px 0 22px;
    background: var(--orange-light); color: var(--white);
    font-family: "Fira Sans", sans-serif; font-weight: 500; font-size: 13px;
    line-height: 22px;
    clip-path: polygon(12px 0, 100% 0, 100% 100%, 0 100%);
  }
  .title-band {
    position: absolute; left: 0; right: 18px; top: 118px; height: 36px;
    background: linear-gradient(90deg, var(--green) 0%, var(--green-light) 100%);
    color: var(--white); font-size: 19px; line-height: 36px; padding-left: 30px;
  }
  .audience-band {
    position: absolute; left: 4px; top: 158px; height: 17px; width: 180px;
    background: var(--orange); color: var(--white);
    font-size: 10px; letter-spacing: .6px; line-height: 17px; padding-left: 29px;
    clip-path: polygon(0 0, 100% 0, calc(100% - 14px) 100%, 0 100%);
  }
  .maker {
    position: absolute; left: 36px; top: 212px;
    color: var(--orange); font-size: 14px; letter-spacing: .6px;
  }
  .base-rule {
    position: absolute; left: 0; right: 0; top: 230px; height: 1.5px; background: var(--green-line);
  }
  .pet-illustration {
    position: absolute; right: 30px; top: 142px; width: 96px; height: 100px;
    background: radial-gradient(ellipse at center, #e7f3df 0%, #f4faf0 70%, var(--white) 100%);
  }

  /* Side panel */
  .panel-side {
    position: absolute; left: 209px; top: 610px; width: 300px; height: 330px;
    background: var(--white);
  }
  .side-brand {
    position: absolute; left: 28px; top: 34px;
    color: var(--green); font-size: 22px; line-height: 1;
  }
  .side-brand sup { font-size: 7px; vertical-align: top; margin-left: 2px; }
  .side-story {
    position: absolute; left: 28px; right: 22px; top: 198px;
    font-family: "Fira Sans", sans-serif; font-style: italic; font-weight: 500;
    color: var(--orange); font-size: 11.5px; line-height: 1.45;
  }
  .side-story strong { font-weight: 700; }
  .side-rule {
    position: absolute; left: 0; right: 0; bottom: 22px; height: 1.5px; background: var(--green-line);
  }
</style>
</head>
<body>
  <section class="panel-top">
    <div class="lid-brand">Lumora™</div>
    <div class="lid-rule"></div>
    <div class="lid-tagline">10-Minute Canine &amp; Feline Rapid Test Kit</div>
  </section>

  <section class="panel-front">
    <div class="front-brand">Lumora<sup>TM</sup></div>
    <div class="badge-tests">5 Tests/Kit</div>
    <div class="title-band">10-Minute Canine &amp; Feline Rapid Test Kit</div>
    <div class="audience-band">FOR DOGS AND CATS</div>
    <div class="maker">Ardenfield</div>
    <div class="base-rule"></div>
    <div class="pet-illustration" role="img" aria-label="Green line illustration of a seated dog and cat"></div>
  </section>

  <section class="panel-side">
    <div class="side-brand">Lumora<sup>TM</sup></div>
    <p class="side-story"><strong>Lumora</strong> is made by Ardenfield, our name combines ‘Arden’ for innovation with “field” for open care, representing both intelligent efficacy in our science and reverence for the spirit of life in all creatures.</p>
    <div class="side-rule"></div>
  </section>
</body>
</html>
```